Movie poster for short film: TINDERLOCK

We need a creative, artistic, stylized poster design for our short film TINDERLOCK. We would like to see designs with graphics and bold colors more than photographs. The photographs we are posting are more for reference- you do not have to use them in the poster! We are looking for something clean and simple. The film is a drama so please don't make it funny. The mood of the film is thoughtful and introspective. Name of film should be in all caps. Things to include in the poster:
Name of film: TINDERLOCK
Lantern Hollow Productions
Starring Marisa Kovalenko

Here is a brief plot synopsis: TINDERLOCK follows one night in the life of a rebellious young woman who breaks into a diner after hours with a can of spray paint. Her intentions change after she ends up discovering what's left of a love story.

The movie is somewhat experimental, set to music for part of it with no dialog. The whole movie takes place in an old fashioned diner.

Target Market(s)

Film festival attendees between the ages of 20-50

Industry/Entity Type

Movie

Font styles to use
Sans Serif

Requirements
Must have
• See project description above- also the film is somewhat dark in nature so please don't make it too 'happy' looking.

```html
<!DOCTYPE html>
<html lang="en">
<head>
<meta charset="utf-8">
<title>TINDERLOCK — Poster</title>
<link href="https://fonts.googleapis.com/css2?family=Cutive+Mono&family=Arimo:wght@400&display=swap" rel="stylesheet">
<style>
  :root {
    --night: #0c0b10;
    --night-glow: #1e1430;
    --panel-red: #761a06;
    --panel-warm: #9a3410;
    --panel-olive: #6e6a12;
    --diner-red: #d8350f;
    --diner-deep: #9c1e08;
    --diner-olive: #8a8a1c;
    --diner-plum: #5a1240;
    --paper: #ffffff;
  }
  html, body {
    margin: 0;
    padding: 0;
    overflow: hidden;
    background: var(--night);
  }
  .poster {
    position: relative;
    width: 777px;
    height: 1200px;
    overflow: hidden;
    background: var(--night);
  }
  .night-glow {
    position: absolute;
    left: 0;
    top: 0;
    width: 777px;
    height: 232px;
    background: linear-gradient(90deg, var(--night) 0%, var(--night) 35%, #141a1c 60%, var(--night-glow) 100%);
  }
  .band {
    position: absolute;
    left: 0;
    top: 233px;
    width: 777px;
    height: 777px;
  }
  .diner-scene {
    position: absolute;
    left: 0;
    top: 0;
    width: 461px;
    height: 100%;
    background:
      linear-gradient(160deg, var(--diner-red) 0%, #e2400f 30%, var(--diner-deep) 55%, transparent 56%),
      linear-gradient(100deg, var(--diner-red) 0%, var(--diner-red) 45%, var(--diner-olive) 46%, var(--diner-olive) 62%, var(--diner-plum) 63%, var(--diner-plum) 100%);
  }
  .light-panel {
    position: absolute;
    left: 461px;
    top: 0;
    width: 316px;
    height: 100%;
    background: linear-gradient(180deg, var(--panel-red) 0%, var(--panel-warm) 35%, var(--panel-olive) 60%, var(--panel-red) 100%);
  }
  .title {
    position: absolute;
    right: 84px;
    top: 326px;
    margin: 0;
    font-family: "Cutive Mono", "Courier New", monospace;
    font-weight: 400;
    font-size: 52px;
    line-height: 1;
    letter-spacing: 1px;
    color: var(--paper);
  }
  .credits {
    position: absolute;
    left: 46px;
    top: 1078px;
    margin: 0;
    font-family: "Arimo", Arial, sans-serif;
    font-size: 15px;
    line-height: 22px;
    letter-spacing: 0.3px;
    color: var(--paper);
    text-transform: uppercase;
  }
</style>
</head>
<body>
<main class="poster">
  <div class="night-glow" aria-hidden="true"></div>

  <section class="band">
    <div class="diner-scene" role="img" aria-label="Stylised illustration of an old-fashioned diner counter with red stools in saturated red, olive and plum tones"></div>
    <div class="light-panel" role="img" aria-label="Soft out-of-focus lights in warm orange, olive and rose tones"></div>
  </section>

  <h1 class="title">TINDERLOCK</h1>

  <p class="credits">
    Lantern Hollow Productions<br>
    Starring Marisa Kovalenko
  </p>
</main>
</body>
</html>
```